Business Card Design Project

I need a business card designed with these details on the front along with the logo attached on the front.

Address - 517/ 208 Wendlebury st Pellford
Website - www.brackwoodcarvers.com.au
Email - delmar@brackwoodcarvers.com.au
Fax - 1900 417 562
Mobile - 0471390618
Telephone - 1300627059
Licence number - 864207k

```html
<!DOCTYPE html>
<html lang="en">
<head>
<meta charset="utf-8">
<title>Brackwood Carvers – Business Card</title>
<link rel="stylesheet" href="https://fonts.googleapis.com/css2?family=Tinos:wght@700&display=swap">
<style>
  :root {
    --page: #ffffff;
    --page-edge: #dcdcdc;
    --card-edge: #c4c4c4;
    --earth: #43291f;
    --paper: #ffffff;
    --stone: #e2cfb5;
    --rule-dark: #8c8c8c;
    --rule-light: #ffffff;
  }
  * { margin: 0; padding: 0; box-sizing: border-box; }
  html, body {
    width: 1200px;
    height: 1000px;
    overflow: hidden;
    background: var(--page);
  }
  .canvas {
    position: relative;
    width: 1200px;
    height: 1000px;
    border: 2px solid var(--page-edge);
  }
  .business-card {
    position: absolute;
    left: 46px;
    top: 158px;
    width: 1112px;
    height: 686px;
    border: 1px solid var(--card-edge);
    display: block;
  }
  .card-text {
    font-family: "Tinos", "Times New Roman", serif;
    font-weight: 700;
  }
  .brand-name {
    fill: var(--earth);
    font-size: 54px;
    letter-spacing: 3px;
  }
  .licence {
    fill: var(--paper);
    font-size: 25px;
    letter-spacing: 0.5px;
  }
  .contact-line {
    fill: var(--paper);
    font-size: 25px;
    letter-spacing: 1.6px;
  }
</style>
</head>
<body>
<main class="canvas">
  <svg class="business-card" viewBox="0 0 1110 684" xmlns="http://www.w3.org/2000/svg" aria-label="Brackwood Carvers business card">
    <defs>
      <linearGradient id="rule-shade" x1="0" x2="1" y1="0" y2="0">
        <stop offset="0" stop-color="var(--rule-dark)"/>
        <stop offset="1" stop-color="var(--rule-light)"/>
      </linearGradient>
    </defs>

    <rect class="card-base" width="1110" height="684" fill="var(--earth)"/>
    <path class="paper-sweep" d="M0,0 L644,0 C712,62 742,150 708,240 C640,400 260,560 0,677 Z" fill="var(--paper)"/>

    <g class="brand" transform="rotate(-29 142 394)">
      <rect class="brand-square" x="72" y="324" width="140" height="140" fill="var(--stone)"/>
    </g>
    <g class="brand-lockup" transform="rotate(-29 225 300)">
      <text class="card-text brand-name" x="225" y="300">BRACKWOOD</text>
      <text class="card-text brand-name" x="240" y="372">CARVERS</text>
    </g>

    <text class="card-text licence" x="713" y="77">Licence Number: 864207k</text>

    <rect class="contact-rule" x="487" y="440" width="7" height="203" fill="url(#rule-shade)"/>
    <g class="contact-details">
      <text class="card-text contact-line" x="504" y="462">517/ 208 Wendlebury st Pellford</text>
      <text class="card-text contact-line" x="504" y="497">www.brackwoodcarvers.com.au</text>
      <text class="card-text contact-line" x="504" y="533">delmar@brackwoodcarvers.com.au</text>
      <text class="card-text contact-line" x="504" y="568">Fax: 1900 417 562</text>
      <text class="card-text contact-line" x="504" y="603">Mobile: 0471390618</text>
      <text class="card-text contact-line" x="504" y="639">Telephone: 1300627059</text>
    </g>
  </svg>
</main>
</body>
</html>
```